Mini Leporello with Tartar Recipe from Christmas Apéro

As present from our christmas apero we would like to give our visitors a little booklet of the tartar recipes they enjoyed with us. For this we need a little pocket recipe booklet. ISt should be a Mini-Leparello. You can find the content attached.

Target Market(s)

customers christmas apero

Font styles to use
Other font styles liked:
• FS albert

Requirements
Must have
• each recipe comes from Kalmor or Markus Brenwil - it should show the author
• the format should be 85 x 85 mm and I need a printable file

```html
<!DOCTYPE html>
<html lang="de">
<head>
<meta charset="utf-8">
<title>Tartar-Rezepte – Leporello</title>
<link rel="stylesheet" href="https://fonts.googleapis.com/css2?family=Roboto+Condensed:wght@400;700&family=Roboto:wght@300;400;700&display=swap">
<style>
  :root {
    --page: #2b211b;
    --red-light: #b3121c;
    --red-deep: #5c0508;
    --black: #0a0505;
    --white: #ffffff;
    --text-soft: #f3e6e6;
    --brand-red: #d9101a;
    --photo-warm: #7a4a2c;
    --photo-plate: #6e6a66;
  }
  html, body { margin: 0; padding: 0; }
  body {
    width: 1200px; height: 1200px; overflow: hidden;
    background: var(--page);
    font-family: "Roboto", sans-serif;
    color: var(--white);
    position: relative;
  }
  .spread { position: absolute; left: 100px; width: 1000px; height: 340px; display: flex; }
  .spread--top { top: 30px; }
  .spread--cover { top: 430px; }
  .spread--bottom { top: 830px; }

  .panel {
    position: relative; width: 500px; height: 340px; overflow: hidden;
    background: radial-gradient(ellipse at 25% 45%, var(--red-light) 0%, var(--red-deep) 55%, var(--black) 100%);
  }
  .recipe-title {
    position: absolute; left: 28px; top: 22px; margin: 0;
    font-family: "Roboto Condensed", sans-serif; font-weight: 400;
    font-size: 36px; line-height: 1;
  }
  .recipe-intro {
    position: absolute; left: 30px; top: 72px; margin: 0;
    font-weight: 300; font-size: 14px; color: var(--text-soft); width: 320px;
  }
  .recipe-intro--large { font-size: 16px; line-height: 1.15; }
  .recipe-intro--small { font-size: 8.5px; line-height: 1.3; width: 300px; top: 66px; }
  .ingredients {
    position: absolute; left: 30px; margin: 0; padding: 0; list-style: none;
    font-weight: 300; font-size: 15px; line-height: 19.5px; color: var(--text-soft);
  }
  .ingredients li::before { content: "●"; font-size: 9px; margin-right: 5px; vertical-align: 2px; }

  .baubles {
    position: absolute; top: 0; right: 20px; width: 120px; height: 160px;
    background: radial-gradient(circle at 60% 70%, #e2303a 0%, #a80e16 30%, rgba(120,5,10,0) 60%);
  }
  .food-photo { position: absolute; border-radius: 50% 50% 0 0 / 40% 40% 0 0; }

  .cover-back, .cover-front {
    background: radial-gradient(ellipse at 35% 45%, #4a3416 0%, #1c120a 45%, var(--black) 100%);
  }
  .brand { display: flex; align-items: center; gap: 8px; font-weight: 700; color: var(--white); }
  .brand__mark { width: 14px; height: 14px; background: var(--brand-red); }
  .cover-back .brand { position: absolute; left: 250px; top: 200px; font-size: 26px; }
  .cover-back__tagline {
    position: absolute; left: 120px; top: 290px; margin: 0;
    font-size: 15px; font-weight: 400;
  }
  .cover-front .brand { position: absolute; left: 300px; top: 40px; font-size: 30px; }
  .cover-title {
    position: absolute; right: 30px; top: 130px; margin: 0; text-align: center; width: 330px;
    font-weight: 400;
  }
  .cover-title__kicker { display: block; font-size: 22px; letter-spacing: 0.5px; }
  .cover-title__venue { display: block; font-weight: 700; font-size: 50px; line-height: 1.05; }
  .cover-title__event { display: block; font-weight: 300; font-size: 26px; letter-spacing: 1px; }
  .cover-title__year { display: block; font-weight: 300; font-size: 28px; letter-spacing: 14px; }
</style>
</head>
<body>

<section class="spread spread--top">
  <article class="panel">
    <h2 class="recipe-title">Rindertartar</h2>
    <p class="recipe-intro">Alle Zutaten fein hacken und mischen :</p>
    <ul class="ingredients" style="top:98px">
      <li>Rindsfilet</li><li>Essiggurken</li><li>Oliven</li><li>Peperoni</li><li>Kapern</li>
      <li>Zwiebel</li><li>Essig</li><li>Senf</li><li>Pfeffer</li><li>Salz</li>
    </ul>
    <div class="baubles" style="right:100px;width:150px;height:220px" role="img" aria-label="Rote Christbaumkugeln an Bändern"></div>
    <div class="food-photo" style="left:240px;top:140px;width:290px;height:220px;border-radius:50%;background:radial-gradient(circle at 45% 45%,#6b2a1e 0%,#4e4b48 45%,#3a3836 70%)" role="img" aria-label="Rindertartar auf grauem Teller"></div>
  </article>
  <article class="panel">
    <h2 class="recipe-title">Ligurisches Kalbstartar</h2>
    <p class="recipe-intro">Alle Zutaten fein hacken und mischen :</p>
    <ul class="ingredients" style="top:96px">
      <li>Kalbfleisch</li><li>Zitronen</li><li>Olivenoel</li><li>Knoblauch</li><li>Pfeffer</li>
      <li>Salz</li><li>Grosszügig Parmesansplitter</li>
    </ul>
    <div class="baubles" role="img" aria-label="Rote Christbaumkugeln an Bändern"></div>
    <div class="food-photo" style="left:300px;top:190px;width:200px;height:150px;background:radial-gradient(circle at 40% 40%,#8a3a34 0%,#6f6a3c 55%,#3b3a22 100%)" role="img" aria-label="Kalbstartar mit Parmesan"></div>
  </article>
</section>

<section class="spread spread--cover">
  <article class="panel cover-back" role="img" aria-label="Goldene Christbaumkugel mit Lichterbokeh">
    <div class="brand"><span class="brand__mark"></span>Kalmor</div>
    <p class="cover-back__tagline">Tartar-Rezepte vom Sternhof Weihnachtsapéro 2016</p>
  </article>
  <article class="panel cover-front" role="img" aria-label="Christbaumkugel mit Lichterbokeh">
    <div class="brand"><span class="brand__mark"></span>Kalmor</div>
    <h1 class="cover-title">
      <span class="cover-title__kicker">TARTAR-REZEPTE VOM</span>
      <span class="cover-title__venue">Sternhof</span>
      <span class="cover-title__event">WEIHNACHTSAPÉRO</span>
      <span class="cover-title__year">2016</span>
    </h1>
  </article>
</section>

<section class="spread spread--bottom">
  <article class="panel">
    <h2 class="recipe-title">Lachstartar</h2>
    <p class="recipe-intro recipe-intro--large">Geräuchter Lachs fein hacken und mit allen Zutaten mischen.</p>
    <ul class="ingredients" style="top:118px;font-size:16px;line-height:22px">
      <li>Geräuchter Lachs</li><li>Sauerrahm</li><li>Dill</li>
    </ul>
    <div class="baubles" role="img" aria-label="Rote Christbaumkugeln an Bändern"></div>
    <div class="food-photo" style="left:70px;top:220px;width:430px;height:130px;background:linear-gradient(90deg,#c9c7b8 0%,#e0703a 30%,#d8d3c4 60%,#bfa77a 100%)" role="img" aria-label="Lachstartar-Türmchen und Frühlingsrollen"></div>
  </article>
  <article class="panel">
    <h2 class="recipe-title">Thunatartar Asiatisch</h2>
    <p class="recipe-intro recipe-intro--small">Den Käse entrinden und in kleine Würfelchen schneiden, Lauch blanchieren, kalt abschrecken. Petersilie und Radieschen hacken danach alle Zutaten mischen und anrichten.</p>
    <ul class="ingredients" style="top:112px;line-height:20.5px">
      <li>Halbhartkäse</li><li>Radieschen</li><li>Petersilie Glattblätterig</li><li>Lauch</li>
      <li>Weinessig</li><li>Senf</li><li>Schwarzer Pfeffer</li><li>Rapsöl</li><li>Rahm</li>
    </ul>
    <div class="baubles" role="img" aria-label="Rote Christbaumkugeln an Bändern"></div>
    <div class="food-photo" style="left:250px;top:170px;width:250px;height:170px;background:radial-gradient(circle at 50% 35%,#c98a8a 0%,#9fb24a 35%,#55545a 65%,#2a2a2e 100%)" role="img" aria-label="Thunfischtartar auf dunklem Teller"></div>
  </article>
</section>

</body>
</html>
```